Birchway Cleaning Commercial Flyer

Would like a flyer that will be used for making sales calls for commercial clients. These flyers will be handed out to Business Owners and facility managers. The flyer must peak interest, introduce the company, and give some information about our services. Birchway Cleaning Services (BWS) is a modern company that is eco-friendly. I have added what the uniform shirt looks like we have one in orange and one in blue. It would be nice to see the pictures you choose have the uniform on.

Target Market(s)

Office Mangers and Facility managers

Industry/Entity Type

Office Cleaning

Font styles to use
Serif

Colors
f78f20
0355a3
abd037

Requirements
Must have
• Modern clean look and feel. The flyer must straight forward and not busy.
• Have sections where bullet points or other written information can be placed
• Must be able to add and move information myself after the design has been decided on.
• Have a section that says:
• To learn more call 301-555-0148 or email info@birchway-tidyco.example
Nice to have
• Some pictures, clean and modern. Peak interest. The uniform to be photoshopped onto the models of the pictures
Should not have
• too busy

```html
<!DOCTYPE html>
<html lang="en">
<head>
<meta charset="utf-8">
<title>Birchway Cleaning Services – Commercial Flyer</title>
<link href="https://fonts.googleapis.com/css2?family=Montserrat:wght@400;500;600;700&display=swap" rel="stylesheet">
<style>
  :root {
    --orange: #f78f20;
    --blue: #0355a3;
    --green: #abd037;
    --ink: #111111;
    --white: #ffffff;
    --mist: #e6e6e6;
    --sky-faint: #e4f1f8;
  }
  * { margin: 0; padding: 0; box-sizing: border-box; }
  html, body { width: 927px; height: 1200px; overflow: hidden; background: var(--white); }
  body { font-family: "Montserrat", Arial, sans-serif; color: var(--ink); }

  .flyer {
    position: relative;
    width: 927px;
    height: 1200px;
    overflow: hidden;
    background: linear-gradient(to bottom, var(--mist) 0, var(--white) 110px, var(--white) 100%);
  }

  .backdrop { position: absolute; inset: 0; width: 927px; height: 1200px; }

  .brand {
    position: absolute;
    left: 100px;
    top: 212px;
    display: flex;
    align-items: center;
    gap: 12px;
  }
  .brand-dot {
    width: 22px; height: 22px; border-radius: 50%;
    background: var(--orange);
  }
  .brand-name {
    font-size: 26px;
    font-weight: 600;
    color: var(--blue);
    letter-spacing: -0.2px;
  }

  .intro {
    position: absolute;
    left: 95px;
    top: 307px;
    width: 460px;
    font-size: 18.5px;
    font-weight: 500;
    line-height: 29px;
    color: var(--ink);
  }

  .photo-round {
    position: absolute;
    left: 583px; top: 58px;
    width: 284px; height: 284px;
    border-radius: 50%;
    border: 6px solid var(--white);
    box-shadow: 0 0 0 10px rgba(255,255,255,0.6);
    background: linear-gradient(160deg, #cfd8c8 0%, #8fa37a 45%, #6a6a72 75%, #3b4f9a 100%);
  }

  .photo-team {
    position: absolute;
    left: 560px; top: 356px;
    width: 325px; height: 672px;
    border-radius: 150px 150px 30px 30px;
    background: linear-gradient(180deg, #c9a58f 0%, #8fb8d8 25%, #3b57d6 50%, #35405a 80%, #d9d9df 100%);
    opacity: 0.92;
  }

  .services {
    position: absolute;
    left: 95px;
    top: 720px;
    color: var(--blue);
  }
  .services-title {
    font-size: 28px;
    font-weight: 700;
    margin-left: 18px;
    margin-bottom: 16px;
    letter-spacing: 0.2px;
  }
  .service-list { list-style: none; }
  .service-item {
    position: relative;
    padding-left: 22px;
    font-size: 22px;
    font-weight: 500;
    line-height: 42px;
    margin-bottom: 12px;
  }
  .service-item svg {
    position: absolute; left: 0; top: 17px;
    width: 12px; height: 10px;
  }

  .contact {
    position: absolute;
    left: 393px;
    top: 1106px;
    color: var(--white);
    font-size: 22px;
    font-weight: 500;
    line-height: 36px;
  }
  .contact-phone { font-size: 28px; font-weight: 700; }
</style>
</head>
<body>
<main class="flyer">

  <svg class="backdrop" viewBox="0 0 927 1200" aria-hidden="true">
    <defs>
      <linearGradient id="band-green" x1="0" y1="0" x2="1" y2="0">
        <stop offset="0" stop-color="#9cc83a"/>
        <stop offset="0.55" stop-color="#cfe59a"/>
        <stop offset="1" stop-color="#9cc83a"/>
      </linearGradient>
    </defs>
    <circle class="halo-ring" cx="330" cy="900" r="290" fill="none" stroke="var(--sky-faint)" stroke-width="26"/>
    <polygon class="band-green" points="0,562 0,598 927,753 927,676" fill="url(#band-green)"/>
    <polygon class="band-orange" points="0,1156 927,1031 927,1200 0,1200" fill="var(--orange)"/>
  </svg>

  <div class="photo-round" role="img" aria-label="Photo of a cleaner in blue uniform pressure-washing a garden patio"></div>

  <div class="brand">
    <span class="brand-dot"></span>
    <span class="brand-name">Birchway Cleaning Services</span>
  </div>

  <p class="intro">Lorem ipsum dolor sit amet, consectetuer adipiscing elit, sed diam nonummy nibh euismod tincidunt ut laoreet dolore magna aliquam erat volutpat. Ut wisi enimLorem ipsum dolor sit amet, consectetuer adipiscing elit, sed diam nonummy nibh euismod tincidunt ut laoreet dolore magna aliquam erat volutpat. Ut wisi enim</p>

  <div class="photo-team" role="img" aria-label="Photo of two smiling cleaners in blue aprons holding mops"></div>

  <section class="services">
    <h2 class="services-title">OUR SERVICES:</h2>
    <ul class="service-list">
      <li class="service-item"><svg viewBox="0 0 12 10"><path d="M1.5 5 L4.5 8 L10.5 2" fill="none" stroke="var(--blue)" stroke-width="2"/></svg>Hospital Grade disinfectants</li>
      <li class="service-item"><svg viewBox="0 0 12 10"><path d="M1.5 5 L4.5 8 L10.5 2" fill="none" stroke="var(--blue)" stroke-width="2"/></svg>Eco-Friendly- microfiber cloths</li>
      <li class="service-item"><svg viewBox="0 0 12 10"><path d="M1.5 5 L4.5 8 L10.5 2" fill="none" stroke="var(--blue)" stroke-width="2"/></svg>HEPA Backpack Vacuums</li>
      <li class="service-item"><svg viewBox="0 0 12 10"><path d="M1.5 5 L4.5 8 L10.5 2" fill="none" stroke="var(--blue)" stroke-width="2"/></svg>Healthy Office/Work Environment<br>is Happy Office</li>
    </ul>
  </section>

  <p class="contact">To learn more call <span class="contact-phone">301-555-0148</span><br>or email info@birchway-tidyco.example</p>

</main>
</body>
</html>
```